Belmora Wines

Hi all,

My name’s Tom Welling and I run a small wine brand based in the Canberra Wine District, Australia. I’m currently in the process of branding the business and am looking for a designer to help develop a new visual direction.

Background
I’ll be growing my own fruit from a leased vineyard site Named 'Ashbrook' and my family’s property named 'Tallin Park', with a stronger emphasis on organic practices and site expression.

The Direction
The brand will centre around single vineyard wines, with each wine reflecting the unique site it comes from. I’d like the branding to support this idea of place, origin, and authenticity.

In terms of visual style, I’m drawn to something that is:

Simple and effective
A balance between traditional and modern
Clean, considered, and not overly decorative

Nothing too over-the-top, the goal is something timeless that lets the wine and vineyard story speak for itself.

At this stage, I’m mainly looking for:

Conceptual design direction / ideas
Label design (with potential to expand into broader branding)

I’m open to creative interpretation, so if the story resonates with you, I’d love to see how you would approach it.

Below I've attached an example of the bottle shape I will be using.

Cheers,
Tom

Colors
0054AA
0677BA
7BADD7
CADEEF
E8F1F8
FFC000
F8CF3A
FAE287
FDF2CF
FEFAEE

Requirements
Must have
• Mix of modern and traditional

```html
<!DOCTYPE html>
<html lang="en">
<head>
<meta charset="utf-8">
<title>Belmora Wines – Tallin Park Shiraz Label</title>
<link rel="stylesheet" href="https://fonts.googleapis.com/css2?family=Libre+Caslon+Text:wght@400&display=swap">
<style>
  :root {
    --backdrop: #000000;
    --sketch-light: #a9abad;
    --sketch-mid: #8d8f92;
    --gold-dark: #6a5a46;
    --gold-light: #b89e74;
    --torn-grey: #a6a8ab;
    --label-ink: #f7f3ec;
  }
  html, body {
    margin: 0;
    padding: 0;
    width: 1200px;
    height: 4536px;
    overflow: hidden;
    background: var(--backdrop);
  }
  .canvas {
    position: relative;
    width: 1200px;
    height: 4536px;
    background: var(--backdrop);
  }
  .label {
    position: absolute;
    left: 0;
    top: 1390px;
    width: 1200px;
    height: 1755px;
    overflow: hidden;
    font-family: "Libre Caslon Text", "Times New Roman", serif;
    color: var(--label-ink);
  }
  .label-art {
    position: absolute;
    inset: 0;
    width: 1200px;
    height: 1755px;
  }
  .label-text {
    position: absolute;
    left: 0;
    width: 1200px;
    text-align: center;
    margin: 0;
    font-weight: 400;
    white-space: nowrap;
  }
  .brand-name {
    top: 1168px;
    font-size: 54px;
    letter-spacing: 0.04em;
    left: 34px;
  }
  .vineyard-name {
    top: 1372px;
    font-size: 48px;
    letter-spacing: 0.01em;
    left: 30px;
  }
  .vineyard-type {
    top: 1440px;
    font-size: 32px;
    letter-spacing: 0.42em;
    left: 30px;
  }
  .varietal {
    top: 1490px;
    font-size: 44px;
    left: 30px;
  }
  .region {
    top: 1684px;
    font-size: 31px;
    letter-spacing: 0.33em;
    left: 30px;
  }
</style>
</head>
<body>
<main class="canvas">
  <section class="label">
    <svg class="label-art" viewBox="0 0 1200 1755" xmlns="http://www.w3.org/2000/svg">
      <defs>
        <linearGradient id="sketch-tone" x1="0" y1="0" x2="0" y2="1">
          <stop offset="0" stop-color="var(--sketch-light)"/>
          <stop offset="1" stop-color="var(--sketch-mid)"/>
        </linearGradient>
        <linearGradient id="gold-field" x1="0" y1="0" x2="1" y2="0">
          <stop offset="0" stop-color="var(--gold-dark)"/>
          <stop offset="1" stop-color="var(--gold-light)"/>
        </linearGradient>
      </defs>
      <rect class="vineyard-sketch" x="0" y="0" width="1200" height="1755" fill="url(#sketch-tone)" role="img" aria-label="Engraved sketch of rolling vineyard hills with farmhouses and cypress trees"/>
      <path class="gold-field" fill="url(#gold-field)"
        d="M0 700 L40 690 L70 640 L120 665 L160 600 L185 640 L230 650 L280 615 L330 655 L390 640
           L420 615 L470 650 L520 620 L560 605 L600 640 L650 610 L700 585 L760 600 L800 560
           L860 585 L900 550 L950 570 L1000 540 L1040 575 L1080 555 L1120 520 L1160 545 L1200 510
           L1200 1755 L0 1755 Z"/>
      <path class="torn-edge" fill="var(--torn-grey)"
        d="M0 1010 L180 1075 L185 1115 L140 1130 L165 1230 L190 1250 L195 1330 L215 1380
           L150 1320 L120 1270 L90 1285 L60 1240 L30 1240 L0 1260 Z"/>
    </svg>
    <p class="label-text brand-name">Belmora Wines</p>
    <p class="label-text vineyard-name">TALLIN PARK</p>
    <p class="label-text vineyard-type">Single Vineyard</p>
    <p class="label-text varietal">Shiraz (2023)</p>
    <p class="label-text region">Canberra Wine District</p>
  </section>
</main>
</body>
</html>
```